Tolvane's 50th Anniversary Gala

Need a cool invitation to be printed on #120 paper for a nonprofit gala fundraiser. Verbiage for invitation is below. Event logo is attached. Could potentially use black and gold but NOT a requirement. Want it to be FUN and DIFFERENT.

Colors
0054AA
0677BA
7BADD7
CADEEF
E8F1F8

```html
<!DOCTYPE html>
<html lang="en">
<head>
<meta charset="utf-8">
<title>Tolvane's 50th Anniversary Gala</title>
<link rel="stylesheet" href="https://fonts.googleapis.com/css2?family=Poppins:wght@400;500;600;700&family=Great+Vibes&display=swap">
<style>
  :root {
    --ink: #000000;
    --gold: #d6ae58;
    --gold-light: #efd48e;
    --gold-pale: #f4e6b8;
    --panel-top: #48474a;
    --panel-mid: #5f5c55;
    --panel-bottom: #4a494b;
  }
  html, body {
    margin: 0;
    padding: 0;
    width: 827px;
    height: 1200px;
    overflow: hidden;
    background: var(--ink);
  }
  .invitation {
    position: relative;
    width: 827px;
    height: 1200px;
    background: var(--ink);
    font-family: "Poppins", sans-serif;
    color: var(--gold);
    overflow: hidden;
  }
  .confetti-panel {
    position: absolute;
    top: 0;
    width: 174px;
    height: 1200px;
    background:
      radial-gradient(circle at 40% 30%, rgba(214,174,88,0.35), transparent 60%),
      radial-gradient(circle at 60% 75%, rgba(214,174,88,0.3), transparent 60%),
      linear-gradient(180deg, var(--panel-top), var(--panel-mid) 50%, var(--panel-bottom));
  }
  .confetti-panel--left { left: 0; }
  .confetti-panel--right { left: 654px; width: 173px; }
  .gold-rule {
    position: absolute;
    top: 0;
    width: 2px;
    height: 1200px;
    background: var(--gold);
  }
  .gold-rule--left { left: 185px; }
  .gold-rule--right { left: 642px; }
  .content {
    position: absolute;
    left: 187px;
    width: 455px;
    top: 0;
    height: 1200px;
    text-align: center;
  }
  .line {
    position: absolute;
    left: 0;
    right: 0;
    margin: 0;
    white-space: nowrap;
  }
  .welcome { top: 194px; font-size: 23px; font-weight: 400; }
  .event-mark {
    position: absolute;
    top: 290px;
    left: 0;
    right: 0;
    display: flex;
    justify-content: center;
    align-items: center;
    gap: 14px;
  }
  .event-mark__dot {
    width: 22px;
    height: 22px;
    border-radius: 50%;
    background: var(--gold-light);
  }
  .event-mark__name {
    font-size: 58px;
    font-weight: 600;
    color: var(--gold-light);
    letter-spacing: 1px;
    line-height: 1;
  }
  .title { top: 440px; font-size: 40px; font-weight: 700; color: var(--gold-light); }
  .when { top: 544px; font-size: 23px; line-height: 29px; font-weight: 400; }
  .when sup { font-size: 12px; }
  .venue { top: 678px; font-family: "Great Vibes", cursive; font-size: 48px; line-height: 60px; }
  .address { top: 736px; font-size: 23px; font-weight: 500; }
  .drink-icon { position: absolute; top: 818px; left: 196px; }
  .fare { top: 942px; font-size: 23px; font-weight: 500; }
  .notes { top: 982px; font-size: 17px; font-weight: 500; }
  .notes .dress { position: absolute; left: 28px; color: var(--gold-pale); }
  .notes .tickets { position: absolute; left: 175px; }
</style>
</head>
<body>
<main class="invitation">
  <div class="confetti-panel confetti-panel--left" role="img" aria-label="Gold confetti, stars and streamers on a dark grey background"></div>
  <div class="confetti-panel confetti-panel--right" role="img" aria-label="Gold confetti, stars and streamers on a dark grey background"></div>
  <div class="gold-rule gold-rule--left"></div>
  <div class="gold-rule gold-rule--right"></div>

  <section class="content">
    <p class="line welcome">Join us for a memorable night!</p>

    <div class="event-mark">
      <span class="event-mark__dot"></span>
      <span class="event-mark__name">Tolvane</span>
    </div>

    <h1 class="line title">Gala Celebration</h1>

    <p class="line when">Friday<br>November 8<sup>th</sup><br>6:30 – 10 p.m.</p>

    <p class="line venue">The Marlow</p>
    <p class="line address">1420 Linden Grove Street</p>

    <svg class="drink-icon" width="62" height="82" viewBox="0 0 62 82" aria-hidden="true">
      <circle cx="15" cy="14" r="13" fill="var(--gold)"/>
      <path d="M6 24 L52 24 L46 44 Q40 54 29 54 Q18 54 12 44 Z" fill="var(--gold)"/>
      <path d="M40 46 L42 10 Q43 4 50 3 L56 2" stroke="var(--gold-light)" stroke-width="3" fill="none"/>
      <rect x="27" y="53" width="4" height="18" fill="var(--gold)"/>
      <path d="M16 79 Q29 68 42 79 Z" fill="var(--gold)"/>
    </svg>

    <p class="line fare">Hors d’oeuvres and Cocktails</p>
    <p class="line notes"><span class="dress">Semi-formal</span><span class="tickets">Ticket information on reverse</span></p>
  </section>
</main>
</body>
</html>
```